New Brochures to deliver confidence of our company to our customers

I would like to have new brochure to be used to distribute to our prospective customers besides the power point presentation. I like the powerpoint you did for us and would like to follow the direction that you have set up. I will attach a number of photos for you to include in our brochure for you to choose. I like the brochure to be modern and forward thinking but just practical. The brochure needs to have three languages which are English, Chinese and Japanese. Attaches is the power point that we like.

Target Market(s)

Multinational companies

Industry/Entity Type

Electronics

Colors

Designer to choose colors to be used in the design.

Requirements
Must have
• Feel lively and modern and yet giving people a sense of confidence. Highlighting the automation is important. Can let us know if you want more photos. The brochure will have three languages, namely english, japanese and chinese.

```html
<!DOCTYPE html>
<html lang="en">
<head>
<meta charset="utf-8">
<title>Norvale Circuits Limited – Brochure Outside Spread</title>
<link href="https://fonts.googleapis.com/css2?family=Exo+2:wght@400;600;700&family=Roboto:wght@300;400&family=Roboto+Condensed:wght@400&display=swap" rel="stylesheet">
<style>
  :root {
    --page-bg: #d4d4d4;
    --panel-dark: #2c3134;
    --panel-dark-2: #23272a;
    --green: #3fb62c;
    --green-bright: #4cc934;
    --red: #e3262b;
    --text-light: #e6e8e8;
    --text-muted: #b8bcbe;
    --grey-heading: #a9adb0;
    --header-white: #f4f5f5;
  }
  * { box-sizing: border-box; margin: 0; padding: 0; }
  html, body { width: 1200px; height: 920px; overflow: hidden; background: var(--page-bg); }
  body { font-family: "Roboto", sans-serif; position: relative; }

  .spread { position: absolute; left: 0; top: 35px; width: 1200px; height: 850px; display: flex; }

  /* Back cover */
  .back-cover {
    position: relative; width: 598px; height: 100%;
    background: linear-gradient(160deg, #31373a 0%, var(--panel-dark) 45%, var(--panel-dark-2) 100%);
    color: var(--text-light);
  }
  .about-title {
    position: absolute; top: 288px; width: 100%; text-align: center;
    font-family: "Roboto", sans-serif; font-weight: 300; font-size: 20px;
  }
  .about-title .accent { color: var(--green); font-weight: 400; }
  .rule { position: absolute; height: 2px; width: 30px; left: 50%; transform: translateX(-50%); }
  .rule-green { background: var(--green); top: 318px; }
  .about-copy { position: absolute; top: 348px; left: 53px; width: 488px; }
  .about-copy p {
    font-weight: 300; font-size: 11.6px; line-height: 15.4px; text-align: justify;
    color: var(--text-light); margin-bottom: 11px;
  }
  .back-brand {
    position: absolute; top: 636px; width: 100%; text-align: center;
    font-family: "Exo 2", sans-serif; font-weight: 700; font-size: 38px; letter-spacing: 3px; color: #ffffff;
  }
  .back-tagline {
    position: absolute; top: 680px; width: 100%; text-align: center;
    font-family: "Roboto Condensed", sans-serif; font-size: 12.5px; color: var(--text-light);
  }
  .touch-title {
    position: absolute; top: 718px; width: 100%; text-align: center;
    font-family: "Roboto Condensed", sans-serif; font-size: 18px; color: #ffffff;
  }
  .touch-title .accent { color: var(--green); }
  .rule-red { background: var(--red); top: 748px; }
  .contact-row {
    position: absolute; width: 100%; display: flex; justify-content: center; gap: 10px;
    font-family: "Roboto Condensed", sans-serif; font-size: 13.5px; color: #ffffff;
  }
  .contact-row.first { top: 768px; }
  .contact-row.second { top: 790px; }
  .contact-item { display: flex; align-items: center; gap: 6px; }
  .contact-item svg { width: 12px; height: 12px; flex: none; }

  /* Front cover */
  .front-cover { position: relative; width: 602px; height: 100%; background: var(--panel-dark); overflow: hidden; }
  .front-header {
    position: absolute; top: 0; left: 0; width: 100%; height: 138px;
    background: radial-gradient(ellipse at center, #ffffff 30%, #e9ebeb 100%);
  }
  .front-brand {
    position: absolute; top: 40px; width: 100%; text-align: center;
    font-family: "Exo 2", sans-serif; font-weight: 700; font-size: 50px; letter-spacing: 4px; color: #1c2a1c;
  }
  .front-tagline {
    position: absolute; top: 108px; width: 100%; text-align: center;
    font-family: "Roboto Condensed", sans-serif; font-size: 11px; letter-spacing: 1.5px; color: #222;
  }
  .factory-photo {
    position: absolute; top: 138px; left: 0; width: 100%; height: 425px;
    background: linear-gradient(180deg, #c9cbc6 0%, #d7d8d2 35%, #b9bdb6 65%, #3f8f4e 100%);
  }
  .front-shapes { position: absolute; top: 0; left: 0; width: 602px; height: 850px; }
  .front-title {
    position: absolute; top: 622px; width: 100%; text-align: center;
    font-family: "Exo 2", sans-serif; font-weight: 400; font-size: 36px; color: var(--green-bright);
  }
  .front-title strong { font-weight: 700; }
  .front-sub {
    position: absolute; top: 680px; width: 100%; text-align: center;
    font-weight: 300; font-size: 14.5px; line-height: 19px; color: var(--text-light);
  }
  .front-claim {
    position: absolute; top: 722px; width: 100%; text-align: center;
    font-family: "Exo 2", sans-serif; font-weight: 700; font-size: 25px; line-height: 30px; color: #ffffff;
  }
  .front-claim .muted { color: var(--grey-heading); }
  .front-claim-rule { position: absolute; top: 793px; left: 50%; width: 60px; height: 1px; transform: translateX(-50%); background: #8a6a3a; }
  .front-web {
    position: absolute; top: 810px; width: 100%; text-align: center;
    font-weight: 300; font-size: 12px; letter-spacing: 8px; color: var(--text-light);
  }
</style>
</head>
<body>
<main class="spread">
  <section class="back-cover">
    <h2 class="about-title">About <span class="accent">Norvale</span></h2>
    <div class="rule rule-green"></div>
    <div class="about-copy">
      <p>Established in 2007, Norvale Circuits Limited (Norvale) is a Hong Kong company specializing in single and double sized printed circuit boards. Its manufacturing facility is located in a self-owned facility in Tangxia, Dongguan of China which is 50 minutes from Hong Kong.</p>
      <p>Our mission is to become a premium low costs PCB supplier that fully embraces human, social and environmental responsibilities.</p>
      <p>Through our insatiable drive to maximize efficiency, Norvale is becoming a highly efficient PCB factory with a capacity of 140,000 sq meter a month.</p>
      <p>PCB is our business and it is through continued automation and innovation that will drive our growth in the next 10 years.</p>
    </div>
    <div class="back-brand">NORVALE</div>
    <div class="back-tagline">Printed Circuit Boards is our Business</div>
    <h3 class="touch-title">GET IN <span class="accent">TOUCH</span></h3>
    <div class="rule rule-red"></div>
    <div class="contact-row first">
      <span class="contact-item"><svg viewBox="0 0 12 12"><path d="M6 0.5a4 4 0 0 0-4 4c0 3 4 7 4 7s4-4 4-7a4 4 0 0 0-4-4z" fill="#e3262b"/><circle cx="6" cy="4.5" r="1.4" fill="#fff"/></svg>Address Goes Here</span>
      <span class="contact-item"><svg viewBox="0 0 12 12"><circle cx="6" cy="6" r="6" fill="#e3262b"/><path d="M4 3.2l1 1.4-.6.7c.4.9 1.1 1.6 2 2l.7-.6 1.4 1-.6 1.1c-2.3-.3-4.2-2.2-4.5-4.5z" fill="#fff"/></svg>0123 456 789</span>
    </div>
    <div class="contact-row second">
      <span class="contact-item"><svg viewBox="0 0 12 12"><circle cx="6" cy="6" r="6" fill="#e3262b"/><rect x="3" y="4" width="6" height="4.2" fill="#fff"/><path d="M3 4l3 2.4L9 4" stroke="#e3262b" stroke-width=".8" fill="none"/></svg>info@yourmailid.com</span>
      <span class="contact-item"><svg viewBox="0 0 12 12"><circle cx="6" cy="6" r="6" fill="#e3262b"/><circle cx="6" cy="6" r="3" fill="none" stroke="#fff" stroke-width=".9"/><path d="M3 6h6M6 3v6" stroke="#fff" stroke-width=".8"/></svg>www.yourwebsite.com</span>
    </div>
  </section>

  <section class="front-cover">
    <div class="front-header"></div>
    <div class="front-brand">NORVALE</div>
    <div class="front-tagline">Printed Circuit Boards is Our Business</div>
    <div class="factory-photo" role="img" aria-label="Photo of an automated PCB production line with white machines in a bright factory hall"></div>
    <svg class="front-shapes" viewBox="0 0 602 850" aria-hidden="true">
      <polygon points="268,138 334,138 301,168" fill="#f1f2f2"/>
      <polygon points="0,563 262,563 301,597 340,563 602,563 602,850 0,850" fill="#2c3134"/>
      <polyline points="0,561 262,561 301,595 340,561 602,561" fill="none" stroke="#3fb62c" stroke-width="5"/>
    </svg>
    <h1 class="front-title"><strong>Norvale</strong> Circuits Limited</h1>
    <p class="front-sub">A premium low cost PCB manufacturer that<br>fully embraces human,</p>
    <p class="front-claim">SOCIAL AND ENVIRONMENTAL<br><span class="muted">RESPONSIBILITIES</span></p>
    <div class="front-claim-rule"></div>
    <p class="front-web">www.yourwebsite.com</p>
  </section>
</main>
</body>
</html>
```